Boutique Shoe Bag Race wear Business Card Design

We are a new luxury shoe bag, jewellery and race wear store stocking local and international designers. Located in the fashion precinct of beautiful Calloway Cove famous in Sydney Australia. Stocking French jewellery and shoes such as Renaud valmiers plus Australian made. Looking at quality and service and looking after the locals and tourists.
Ideas: White background, Black writing in bold engravers, logo in middle of Marlow and Boutique a gold horseshoe (facing upright so the curve is at the bottom) with a black stiletto inside. French clover silver and black border (not irish clover the French lattice type look)
Updates

Marlow Atelier

I open 8/4 so require business card design ASAP.

Please place gold horseshoe facing upwards with the black stiletto inside.

Bold engravers writing for business name.

I will have my phone number tomorrow to update.

Border in similar/same style as attached picture with black/silver clover French design.

Thank you. Tessa                                   

Industry/Entity Type

Fashion

Contact Information for Business Card

Marlow Atelier
Boutique Owner Tessa Wrenfield
41B Parrin Lane
Calloway Cove NSW 2093 Australia
0471239046
02 **** *TBA
info@marlowatelier.com.au
Facebook.com/MarlowAtelier
www.marlowatelier.com.au

Font styles to use
Other font styles liked:
• Bold Engravers

Requirements
Must have
• Info on one side including business name and logo with black stiletto and gold horse shoe. reverse side with French clover border and Larger name Marlow Atelier with logo in centre.
Should not have
• irish clover
French script
horseshoe upside down

```html
<!DOCTYPE html>
<html lang="en">
<head>
<meta charset="utf-8">
<title>Marlow Atelier – Business Card</title>
<link href="https://fonts.googleapis.com/css2?family=Cinzel:wght@700;900&family=Gelasio:ital,wght@0,400;1,400&family=Open+Sans:wght@400&display=swap" rel="stylesheet">
<style>
  :root {
    --gold: #b5a334;
    --gold-dim: #6e6424;
    --ink: #3e3e3e;
    --rule: #c8c8c8;
    --card-border: #c4c4c4;
    --night: #141414;
    --paper: #ffffff;
    --label: #555555;
    --band: #e6e6e6;
  }
  * { margin: 0; padding: 0; box-sizing: border-box; }
  html, body { width: 900px; height: 1200px; overflow: hidden; background: var(--paper); }
  .sheet { position: relative; width: 900px; height: 1200px; }

  .card { position: absolute; left: 41px; width: 818px; height: 505px; }
  .card--front { top: 43px; border: 1px solid var(--card-border); background: var(--paper); }
  .card--back { top: 622px; background: var(--night); }

  .side-label {
    position: absolute; left: 41px;
    font-family: "Open Sans", Arial, sans-serif; font-size: 15px; color: var(--label);
  }
  .side-label--front { top: 553px; }
  .side-label--back { top: 1132px; }

  .brand-mark {
    position: absolute; left: 0; right: 0; top: 70px;
    display: flex; justify-content: center; align-items: center; gap: 10px;
    font-family: "Gelasio", Georgia, serif; font-size: 18px; color: var(--gold);
    letter-spacing: 1px;
  }
  .brand-mark__dot { width: 14px; height: 14px; border-radius: 50%; background: var(--gold); }

  .owner-name {
    position: absolute; left: 0; right: 0; top: 150px; text-align: center;
    font-family: "Cinzel", "Times New Roman", serif; font-weight: 700;
    font-size: 46px; letter-spacing: 2px; color: var(--gold); line-height: 1;
  }
  .name-rule {
    position: absolute; left: 189px; width: 448px; top: 209px;
    border-top: 1px solid var(--rule);
  }
  .owner-title {
    position: absolute; left: 0; right: 0; top: 213px; text-align: center;
    font-family: "Gelasio", Georgia, serif; font-style: italic;
    font-size: 17px; letter-spacing: 1.6px; color: var(--ink);
  }

  .contact {
    position: absolute; top: 275px;
    font-family: "Gelasio", Georgia, serif; font-size: 17px; line-height: 24.5px;
    color: var(--ink); letter-spacing: 0.5px; list-style: none;
  }
  .contact--postal { right: 408px; text-align: right; }
  .contact--online { left: 437px; }

  .border-band {
    position: absolute; left: 29px; width: 758px; top: 428px; height: 42px;
    background: var(--band);
  }

  .back-corner {
    position: absolute; width: 48px; height: 48px;
    background: var(--gold-dim); transform: rotate(45deg);
  }
  .back-corner--tl { left: 44px; top: 42px; }
  .back-corner--tr { right: 44px; top: 42px; }
  .back-corner--bl { left: 40px; bottom: 44px; }
  .back-corner--br { right: 42px; bottom: 42px; }

  .wordmark {
    position: absolute; left: 0; right: 0; top: 222px;
    display: flex; justify-content: center; align-items: center; gap: 28px;
    font-family: "Cinzel", "Times New Roman", serif; font-weight: 900;
    font-size: 40px; letter-spacing: 3px; color: var(--paper);
  }
  .wordmark__dot { width: 62px; height: 62px; border-radius: 50%; background: var(--gold); }
</style>
</head>
<body>
<main class="sheet">
  <section class="card card--front" aria-label="Business card front">
    <div class="brand-mark"><span class="brand-mark__dot"></span>Marlow Atelier</div>
    <h1 class="owner-name">Tessa Wrenfield</h1>
    <div class="name-rule"></div>
    <p class="owner-title">Marlow Atelier Boutique Owner</p>
    <ul class="contact contact--postal">
      <li>41B Parrin Lane Calloway Cove</li>
      <li>NSW 2093 Australia</li>
      <li>0471239046</li>
      <li>02 **** *TBA</li>
    </ul>
    <ul class="contact contact--online">
      <li>info@marlowatelier.com.au</li>
      <li>Facebook.com/MarlowAtelier</li>
      <li>www.marlowatelier.com.au</li>
    </ul>
    <div class="border-band" role="img" aria-label="Border of diamond-framed French lattice clover motifs in silver and black"></div>
  </section>
  <p class="side-label side-label--front">Front side</p>

  <section class="card card--back" aria-label="Business card back">
    <div class="back-corner back-corner--tl" role="img" aria-label="Gold diamond-framed clover motif"></div>
    <div class="back-corner back-corner--tr" role="img" aria-label="Gold diamond-framed clover motif"></div>
    <div class="back-corner back-corner--bl" role="img" aria-label="Gold diamond-framed clover motif"></div>
    <div class="back-corner back-corner--br" role="img" aria-label="Gold diamond-framed clover motif"></div>
    <div class="wordmark"><span>MARLOW</span><span class="wordmark__dot"></span><span>ATELIER</span></div>
  </section>
  <p class="side-label side-label--back">Back side</p>
</main>
</body>
</html>
```